Australian Software Consultancy needs new Business Card Design

Design Business Card based on existing design artefacts (attached). We are open to all designs. As its a 2 sided design and we thought it might be quite striking to have one side with a black background and te other side with a white background.

Target Market(s)

Financial Services mainly.

Industry/Entity Type

Business

Contact Information for Business Card

Name :
Position :
Email :

Requirements
Must have
• Funky design using our existing assets

```html
<!DOCTYPE html>
<html lang="en">
<head>
<meta charset="utf-8">
<title>Inner Field — Business Card</title>
<link rel="stylesheet" href="https://fonts.googleapis.com/css2?family=Titillium+Web:wght@400;600;700&family=Noto+Sans:wght@400;700&display=swap">
<style>
  :root {
    --stage: #ececec;
    --paper: #ffffff;
    --ink: #0b0b0c;
    --accent: #e8222b;
    --muted: #1d1d1f;
  }
  * { box-sizing: border-box; margin: 0; padding: 0; }
  html, body { width: 1200px; height: 1000px; overflow: hidden; }
  body {
    background: var(--stage);
    font-family: "Noto Sans", Arial, sans-serif;
    position: relative;
  }
  .card {
    position: absolute;
    width: 460px;
    height: 270px;
    top: 365px;
    overflow: hidden;
    box-shadow: 0 4px 14px rgba(0,0,0,.18);
  }
  .card-front { left: 110px; background: var(--paper); }
  .card-back { left: 630px; background: var(--ink); }
  .card-shapes { position: absolute; inset: 0; width: 100%; height: 100%; }

  .brand-mark {
    position: absolute;
    left: 28px;
    top: 114px;
    display: flex;
    align-items: center;
    gap: 10px;
  }
  .brand-dot {
    width: 30px; height: 30px;
    border-radius: 50%;
    border: 4px solid var(--accent);
  }
  .brand-name {
    font-family: "Titillium Web", Arial, sans-serif;
    font-weight: 700;
    font-size: 22px;
    letter-spacing: 1px;
    color: var(--accent);
    text-transform: uppercase;
  }

  .contact {
    position: absolute;
    left: 215px;
    top: 78px;
    color: var(--muted);
  }
  .contact-name {
    font-family: "Titillium Web", Arial, sans-serif;
    font-weight: 700;
    font-size: 21px;
    line-height: 1;
    color: var(--ink);
  }
  .contact-name .surname { color: var(--accent); }
  .contact-role { font-size: 14px; margin: 3px 0 8px; }
  .contact-list { list-style: none; }
  .contact-list li {
    display: flex; align-items: center; gap: 8px;
    font-size: 10.5px; line-height: 16px;
  }
  .contact-list li.phone { font-size: 12.5px; }
  .contact-list svg { width: 11px; height: 11px; fill: var(--accent); flex: none; }

  .back-title {
    position: absolute;
    inset: 0;
    display: flex;
    align-items: center;
    justify-content: center;
    font-family: "Titillium Web", Arial, sans-serif;
    font-weight: 700;
    font-size: 38px;
    letter-spacing: 1px;
    color: var(--paper);
    text-transform: uppercase;
  }
</style>
</head>
<body>

<section class="card card-front" aria-label="Card front">
  <svg class="card-shapes" viewBox="0 0 460 270" preserveAspectRatio="none">
    <polygon points="0,0 335,0 295,48 0,82" fill="var(--accent)"/>
    <polygon points="30,270 130,228 460,190 460,270" fill="var(--ink)"/>
  </svg>

  <div class="brand-mark">
    <span class="brand-dot"></span>
    <span class="brand-name">Inner Field</span>
  </div>

  <div class="contact">
    <p class="contact-name">JOHN <span class="surname">DOE</span></p>
    <p class="contact-role">Director</p>
    <ul class="contact-list">
      <li class="phone">
        <svg viewBox="0 0 24 24"><path d="M6.6 10.8a15 15 0 0 0 6.6 6.6l2.2-2.2c.3-.3.7-.4 1-.2 1.1.4 2.3.6 3.6.6.6 0 1 .4 1 1V20c0 .6-.4 1-1 1A17 17 0 0 1 3 4c0-.6.4-1 1-1h3.5c.6 0 1 .4 1 1 0 1.3.2 2.5.6 3.6.1.3 0 .7-.2 1z"/></svg>
        123 456 789
      </li>
      <li>
        <svg viewBox="0 0 24 24"><path d="M12 2a10 10 0 1 0 0 20 10 10 0 0 0 0-20zm6.9 6h-3a15 15 0 0 0-1.3-3.9A8 8 0 0 1 18.9 8zM12 4c.8 1.2 1.5 2.5 1.9 4h-3.8c.4-1.5 1.1-2.8 1.9-4zM4.3 14a8 8 0 0 1 0-4h3.4a16 16 0 0 0 0 4zm.8 2h3a15 15 0 0 0 1.3 3.9A8 8 0 0 1 5.1 16zm3-8h-3a8 8 0 0 1 4.3-3.9A15 15 0 0 0 8.1 8zM12 20c-.8-1.2-1.5-2.5-1.9-4h3.8c-.4 1.5-1.1 2.8-1.9 4zm2.3-6H9.7a14 14 0 0 1 0-4h4.6a14 14 0 0 1 0 4zm.3 5.9a15 15 0 0 0 1.3-3.9h3a8 8 0 0 1-4.3 3.9zm1.7-5.9a16 16 0 0 0 0-4h3.4a8 8 0 0 1 0 4z"/></svg>
        WWW.YOUESITEGOESHERE.COM
      </li>
      <li>
        <svg viewBox="0 0 24 24"><path d="M2 5h20v14H2zm2 2v.5l8 5 8-5V7zm0 2.8V17h16V9.8l-8 5z"/></svg>
        EMAIL@DOMAINGOESHERE.COM
      </li>
    </ul>
  </div>
</section>

<section class="card card-back" aria-label="Card back">
  <svg class="card-shapes" viewBox="0 0 460 270" preserveAspectRatio="none">
    <polygon points="0,0 460,0 460,14 330,40 100,18 0,30" fill="var(--paper)"/>
    <polygon points="0,270 0,240 95,205 320,225 460,205 460,270" fill="var(--accent)"/>
  </svg>
  <p class="back-title">Inner Field</p>
</section>

</body>
</html>
```